Essential Oil Blend Label Design

I need a label designed for our stress relief essential blend, Marlo's Drift.
The text for the front of the logo will be as follows:
"Marlo's Drift
All Natural Stress and Anxiety Relief
www.corvantglow.com"
Please make the front text small enough that it will show up in a picture of the bottle with the label is applied without being cut off on the edges. For reference, the label will be 4" x 2" and will go on these bottles:
http://www.brindlevessel.com/glass-bottles/european-dropper/amber/30ml-kqt30
On one of the sides of the label I would like this text, going up the label so that you turn the bottle sideways to read it (like in the attached label):
"Contains a pure, undiluted essential oil blend"
On the other side "For use in aromatherapy"
I would like this label to incorporate elements of a lush, green garden, like the Garden of Eden. The goal is for it convey peace and relaxation.
Please also note that I have attached the label for our other product for reference. The new label should be similar in its basic design as far as where the text is present and the overall style. My one problem with the attached label, though, is that the front text is a little too large and doesn't show up all the way in a picture. (I've attached the picture of the bottle as well so you can see what I mean).
I look forward to working with you!
Neil

```html
<!DOCTYPE html>
<html lang="en">
<head>
<meta charset="utf-8">
<title>Willowly Repose – Essential Oil Label</title>
<link href="https://fonts.googleapis.com/css2?family=Anton&family=Oswald:wght@500;700&family=Archivo+Black&display=swap" rel="stylesheet">
<style>
  :root {
    --leaf-deep: #14500c;
    --leaf-dark: #1f6a12;
    --leaf-mid: #3f9e1c;
    --leaf-light: #6fd23a;
    --leaf-bright: #8ee84f;
    --label-white: #ffffff;
    --brand-green: #56ee1b;
    --side-green: #58e81e;
    --navy: #0c1a4b;
  }
  html, body {
    margin: 0;
    padding: 0;
    overflow: hidden;
    background: #ffffff;
  }
  .label {
    position: relative;
    width: 1200px;
    height: 601px;
    overflow: hidden;
  }
  .garden-backdrop {
    position: absolute;
    inset: 0;
    background:
      radial-gradient(circle at 12% 18%, rgba(142,232,79,0.55), transparent 22%),
      radial-gradient(circle at 38% 78%, rgba(142,232,79,0.45), transparent 20%),
      radial-gradient(circle at 62% 22%, rgba(111,210,58,0.55), transparent 24%),
      radial-gradient(circle at 84% 62%, rgba(142,232,79,0.5), transparent 22%),
      radial-gradient(circle at 24% 50%, rgba(20,80,12,0.55), transparent 26%),
      radial-gradient(circle at 74% 88%, rgba(20,80,12,0.5), transparent 24%),
      radial-gradient(circle at 52% 50%, rgba(31,106,18,0.45), transparent 30%),
      linear-gradient(160deg, var(--leaf-mid), var(--leaf-dark) 50%, var(--leaf-mid));
  }
  .side-strip {
    position: absolute;
    top: 0;
    width: 123px;
    height: 601px;
    background: var(--label-white);
  }
  .side-strip--left { left: 25px; }
  .side-strip--right { left: 1052px; }
  .side-text {
    position: absolute;
    margin: 0;
    font-family: "Oswald", "Arial Narrow", sans-serif;
    font-weight: 700;
    font-size: 37px;
    line-height: 40px;
    color: var(--side-green);
    text-align: left;
    white-space: nowrap;
    transform-origin: top left;
  }
  .side-text--claim {
    left: 124px;
    top: 76px;
    width: 470px;
    transform: rotate(90deg);
  }
  .side-text--usage {
    left: 1078px;
    top: 448px;
    width: 300px;
    transform: rotate(-90deg);
  }
  .title-plate {
    position: absolute;
    left: 0;
    top: 0;
  }
  .brand-name {
    position: absolute;
    left: 320px;
    width: 560px;
    margin: 0;
    font-family: "Anton", "Impact", sans-serif;
    font-weight: 400;
    color: var(--brand-green);
    text-align: center;
    line-height: 1;
    font-size: 90px;
    letter-spacing: 10px;
    text-indent: 10px;
    white-space: nowrap;
  }
  .brand-name--top { top: 202px; }
  .brand-name--bottom { top: 300px; }
  .tagline {
    position: absolute;
    left: 300px;
    top: 412px;
    width: 600px;
    margin: 0;
    font-family: "Oswald", "Arial Narrow", sans-serif;
    font-weight: 500;
    font-size: 27px;
    line-height: 40px;
    letter-spacing: 1px;
    color: var(--label-white);
    text-align: center;
    white-space: nowrap;
  }
  .web-address {
    position: absolute;
    left: 350px;
    top: 474px;
    width: 500px;
    height: 52px;
    background: var(--navy);
    color: var(--label-white);
    font-family: "Archivo Black", "Arial Black", sans-serif;
    font-size: 24px;
    letter-spacing: 2px;
    line-height: 52px;
    text-align: center;
  }
</style>
</head>
<body>
  <main class="label">
    <div class="garden-backdrop" role="img" aria-label="Lush garden of dense green clover leaves covering the whole label"></div>

    <div class="side-strip side-strip--left"></div>
    <div class="side-strip side-strip--right"></div>

    <p class="side-text side-text--claim">"Contains a pure, undiluted<br>essential oil blend"</p>
    <p class="side-text side-text--usage">For use<br>in aromatherapy</p>

    <svg class="title-plate" width="1200" height="601" viewBox="0 0 1200 601" aria-hidden="true">
      <polygon points="320,200 880,196 866,302 792,302 792,398 408,398 408,302 334,302" fill="#ffffff"/>
    </svg>

    <h1 class="brand-name brand-name--top">WILLOWLY</h1>
    <p class="brand-name brand-name--bottom">REPOSE</p>

    <p class="tagline">All Natural Stress and Anxiety Relief</p>

    <div class="web-address">www.corvantglow.com</div>
  </main>
</body>
</html>
```